Surface Protection company needs cards

We are a New Zealand company that will apply nanotechnology coatings on surfaces to prevent growth and spread of bacteria, viruses, mold etc with a sprayer. We deal with large corporates, airlines, hospitals and schools so we are after a new modern, simple and clean look that will have great visual impact.
We a company that is focused on prevention and protection.

Company name, Vela Shield

Subtext, Antimicrobial Surface Protection

Logo, VS

Target Market(s)

Hospitals, Transport agencies, Airlines, Corporate entities

Contact Information for Business Card

Company name, VelaShield
Logo, VS

Gareth Tolley
velashieldnz@postbox.example
+64219305562
www.velashield.example.nz

Requirements
Must have
• Simple clean look.
Nice to have
• We apply nano coatings so try and incorporate this into a theme somehow

```html
<!DOCTYPE html>
<html lang="en">
<head>
<meta charset="utf-8">
<title>VelaShield Business Cards</title>
<link href="https://fonts.googleapis.com/css2?family=Montserrat:wght@300;400;600;700&display=swap" rel="stylesheet">
<style>
  :root {
    --page-bg: #1a2436;
    --card-bg: #0f1826;
    --card-edge: #1b2738;
    --brand-blue: #2f86c9;
    --name-blue: #2a7cc4;
    --icon-blue: #2f9bd6;
    --text-light: #eef2f7;
    --text-soft: #c3ccd8;
    --text-muted: #9aa6b6;
    --fabric-light: #5d6f92;
    --fabric-dark: #2a3650;
  }
  * { box-sizing: border-box; margin: 0; padding: 0; }
  html, body {
    width: 1200px; height: 800px; overflow: hidden;
    background: radial-gradient(ellipse at center, #22304a 0%, var(--page-bg) 60%, #111a29 100%);
    font-family: "Montserrat", Arial, sans-serif;
  }
  .sheet {
    width: 1200px; height: 800px;
    display: flex; align-items: center; justify-content: center; gap: 40px;
  }
  .card {
    position: relative;
    width: 540px; height: 310px;
    background: linear-gradient(160deg, #152133 0%, var(--card-bg) 70%);
    border: 1px solid var(--card-edge);
    box-shadow: 0 20px 40px rgba(0,0,0,0.45);
    overflow: hidden;
  }

  /* Front card */
  .front-photo {
    position: absolute; right: 0; bottom: 0;
    width: 340px; height: 230px;
    background:
      radial-gradient(ellipse at 65% 55%, var(--fabric-light) 0%, rgba(74,90,124,0.6) 35%, rgba(42,54,80,0.2) 65%, transparent 85%);
  }
  .front-brand {
    position: absolute; left: 36px; top: 44px;
    font-size: 58px; font-weight: 700; letter-spacing: -0.5px;
    color: var(--brand-blue);
  }
  .front-subtext {
    position: absolute; left: 38px; top: 118px; width: 340px;
    font-size: 19px; font-weight: 400; line-height: 1.15;
    color: var(--text-soft);
  }
  .front-web {
    position: absolute; left: 0; right: 0; bottom: 30px;
    text-align: center;
    font-size: 15px; font-weight: 300; letter-spacing: 6px;
    color: var(--text-muted);
  }

  /* Back card */
  .back-head {
    position: absolute; left: 0; right: 0; top: 56px; text-align: center;
  }
  .back-brand {
    font-size: 26px; font-weight: 700; color: var(--text-light);
  }
  .back-name {
    margin-top: 2px;
    font-size: 34px; font-weight: 700; letter-spacing: 2px;
    color: var(--name-blue); text-transform: uppercase;
  }
  .contact-list {
    position: absolute; left: 44px; bottom: 40px;
    list-style: none;
  }
  .contact-item {
    display: flex; align-items: center; gap: 14px;
    font-size: 17px; font-weight: 400; color: var(--text-light);
    margin-top: 8px;
  }
  .contact-icon { width: 20px; height: 20px; flex: none; }
</style>
</head>
<body>
<main class="sheet">

  <section class="card card-front">
    <div class="front-photo" role="img" aria-label="Close-up photo of a water droplet beading on coated fabric"></div>
    <h1 class="front-brand">VelaShield</h1>
    <p class="front-subtext">Subtext, Antimicrobial Surface Protection</p>
    <p class="front-web">www.velashield.example.nz</p>
  </section>

  <section class="card card-back">
    <div class="back-head">
      <p class="back-brand">VelaShield</p>
      <h2 class="back-name">Gareth Tolley</h2>
    </div>
    <ul class="contact-list">
      <li class="contact-item">
        <svg class="contact-icon" viewBox="0 0 24 24" aria-hidden="true">
          <path fill="var(--icon-blue)" d="M6.6 10.8a15.1 15.1 0 0 0 6.6 6.6l2.2-2.2a1 1 0 0 1 1-.25 11.4 11.4 0 0 0 3.6.57 1 1 0 0 1 1 1V20a1 1 0 0 1-1 1A17 17 0 0 1 3 4a1 1 0 0 1 1-1h3.5a1 1 0 0 1 1 1c0 1.25.2 2.45.57 3.57a1 1 0 0 1-.25 1z"/>
        </svg>
        +64219305562
      </li>
      <li class="contact-item">
        <svg class="contact-icon" viewBox="0 0 24 24" aria-hidden="true">
          <rect x="2" y="5" width="20" height="14" fill="var(--icon-blue)"/>
          <path d="M2 5l10 8 10-8" fill="none" stroke="var(--card-bg)" stroke-width="1.6"/>
        </svg>
        velashieldnz@postbox.example
      </li>
      <li class="contact-item">
        <svg class="contact-icon" viewBox="0 0 24 24" aria-hidden="true">
          <circle cx="12" cy="12" r="10" fill="none" stroke="var(--icon-blue)" stroke-width="2"/>
          <ellipse cx="12" cy="12" rx="4" ry="10" fill="none" stroke="var(--icon-blue)" stroke-width="1.6"/>
          <path d="M2 12h20" stroke="var(--icon-blue)" stroke-width="1.6"/>
        </svg>
        www.velashield.example.nz
      </li>
    </ul>
  </section>

</main>
</body>
</html>
```